Audio Visual & Broadcast Installing Company needs a Web Site Design

We need a website design for our company Corvane Ltd. We are a small company that does Audio Visual and broadcast installations. We are looking to expand our business and need a professional web presence. All work completed by us is done to a very high standard and it’s this attention to detail that sets us apart from our competitors. Our projects include doing fibre optics at major sporting events; installing and commissioning bespoke control systems on super yachts and installing the latest systems in luxury homes.

We provide the following services:
System design
On-site installation
Rack building
Pre-fabricated cable looms
Fibre optic cabling

We would like a website that gives details of our services and provides contact information. Our customers are other businesses and our website needs to reflect this. The flyer attached will be used to promote the company and we would like the website to follow this theme. Please use the colours from our logo, as the colour scheme. We know that our colours are bright and we don’t want them to overwhelm the site. With our website we want to communicate that we are professional and provide a quality service.
NB UPDATE: please use stock images for any graphical elements.

The following 3 sites belong to some of our competitors. The first 2, we DON'T like because they don't project a professional feeling. The last one, 'vellumspire', is better as it provides the required information in a clear, simple form.

http://www.plomquist-example.com/

http://www.heronfieldlinkworks-example.com/

http://www.vellumspire-example.com/

We really like the following site, it feels professional and high end without too many flashy graphics. We want something that is fast to load but still shows the high end quality of our work.

http://osmerdalegroup-example.com/

Pages/Sections

Home
On site installation
Rack building and cable looms
Fibre optics
Portfolio (this will be limited to start with but must be easy to expand and add new projects)
Updates

Target Market(s)

Businesses operating in the following areas:
Audio Vision, Broadcasting, Home Automation, Events

Industry/Entity Type

Broadcasting

Coding

Coded - Design and coding required

Number of Pages Required

4 page

Font styles to use
Other font styles liked:
• similar to attached flyer

Requirements
Must have
• The same theme as the 'flyer1' attachment.

```html
<!DOCTYPE html>
<html lang="en">
<head>
<meta charset="utf-8">
<title>Corvane Ltd – Broadcast &amp; AV Installation</title>
<link href="https://fonts.googleapis.com/css2?family=Open+Sans:wght@400;600;700&family=Noto+Serif:wght@700&display=swap" rel="stylesheet">
<style>
:root{
  --blue:#1e88f0;
  --blue-deep:#0f5fc2;
  --pink:#e8175d;
  --red:#e0103f;
  --dark:#222428;
  --ink:#333;
  --white:#fff;
  --muted:#9aa0a8;
}
*{box-sizing:border-box;margin:0;padding:0}
html,body{width:1200px;height:2600px;overflow:hidden}
body{font-family:"Open Sans",Arial,sans-serif;color:var(--ink);background:var(--white);position:relative}

/* Hero */
.hero{position:absolute;left:0;top:0;width:1200px;height:500px;
  background:radial-gradient(ellipse at 60% 55%,#5a6a80 0%,#2c3850 45%,#141a26 100%)}
.brand{position:absolute;display:flex;align-items:center;gap:12px}
.brand-mark{width:34px;height:34px;background:var(--red);border-radius:50%}
.brand-name{font-family:"Open Sans",Arial,sans-serif;font-weight:700;font-size:30px;color:var(--white)}
.hero .brand{left:60px;top:62px}
.social{position:absolute;display:flex;gap:12px}
.social span{width:18px;height:18px;border-radius:50%;background:var(--white)}
.hero .social{right:70px;top:24px}
.main-nav{position:absolute;right:60px;top:76px;display:flex;background:rgba(20,24,34,.85);height:36px;align-items:center;padding-right:40px}
.main-nav a{color:var(--white);text-decoration:none;font-size:15px;padding:0 14px;line-height:36px}
.main-nav a.active{background:var(--red)}
.hero-title{position:absolute;left:50%;top:256px;transform:translateX(-50%);
  background:rgba(20,26,40,.6);color:var(--white);font-weight:700;font-size:30px;padding:10px 22px;white-space:nowrap}
.btn{display:inline-block;background:var(--blue);color:var(--white);font-size:15px;padding:8px 16px;border-radius:3px;text-decoration:none}
.hero .btn{position:absolute;left:540px;top:428px}
.arrow{position:absolute;top:270px;width:36px;height:36px}
.arrow.prev{left:6px}.arrow.next{right:6px}
.dots{position:absolute;left:560px;top:478px;display:flex;gap:10px}
.dots span{width:10px;height:10px;border-radius:50%;background:rgba(255,255,255,.6)}
.dots span:first-child{background:var(--white)}

/* Services */
.services{position:absolute;left:0;top:500px;width:1200px;height:540px;background:var(--blue);color:var(--white);text-align:center}
.section-title{font-weight:700;font-size:30px}
.services .section-title{margin-top:84px}
.services .rule{width:60px;height:3px;background:var(--white);margin:14px auto 0}
.service-list{display:flex;justify-content:space-between;padding:0 90px;margin-top:108px}
.service{width:170px;display:flex;flex-direction:column;align-items:center}
.service-icon{width:76px;height:76px;border-radius:50%;background:var(--white);display:flex;align-items:center;justify-content:center}
.service p{font-size:22px;line-height:1.3;margin-top:22px}

/* About */
.about{position:absolute;left:0;top:1040px;width:1200px;height:420px}
.about h2{position:absolute;left:60px;top:46px;font-size:32px;font-weight:700;color:var(--ink)}
.about .underline{position:absolute;left:60px;top:98px;width:170px;height:3px;background:var(--red)}
.about h3{position:absolute;left:60px;top:140px;width:540px;font-size:23px;line-height:1.4;color:var(--blue-deep);font-weight:700}
.about p{position:absolute;left:60px;top:230px;width:560px;font-size:17px;line-height:1.55}
.btn-red{background:var(--red)}
.about .btn{position:absolute;left:60px;top:330px;font-size:14px;padding:6px 14px}
.video{position:absolute;left:664px;top:60px;width:480px;height:300px;
  background:linear-gradient(135deg,#3c3a3c 0%,#7a6a60 45%,#2a2a30 100%)}

/* What we do */
.what{position:absolute;left:0;top:1460px;width:1200px;height:600px;
  background:linear-gradient(180deg,var(--pink) 0%,var(--pink) 62%,#b8134a 100%)}
.crowd{position:absolute;left:0;bottom:0;width:1200px;height:200px;
  background:linear-gradient(180deg,rgba(232,23,93,0) 0%,rgba(120,10,45,.55) 100%)}
.what h2{position:absolute;left:60px;top:60px;font-size:32px;font-weight:700;color:var(--white)}
.what .underline{position:absolute;left:60px;top:110px;width:200px;height:3px;background:var(--white)}
.what ul{position:absolute;left:60px;top:156px;width:680px;list-style:none;color:var(--white);font-size:15px;line-height:1.45}
.what li{position:relative;padding-left:26px;margin-bottom:11px}
.what li::before{content:"";position:absolute;left:2px;top:6px;border-left:9px solid var(--white);border-top:5px solid transparent;border-bottom:5px solid transparent}
.what .btn{position:absolute;left:60px;top:484px;font-size:14px;padding:7px 12px}
.quote{position:absolute;left:770px;top:1360px;width:370px;height:370px;border-radius:50%;background:var(--blue);
  display:flex;align-items:center;justify-content:center;text-align:center;color:var(--white);
  font-family:"Noto Serif",Georgia,serif;font-weight:700;font-size:35px;line-height:1.3;padding:40px}

/* Footer */
.footer{position:absolute;left:0;top:2060px;width:1200px;height:500px;background:var(--dark);color:var(--white)}
.contact-tab{position:absolute;left:60px;top:30px;background:var(--blue);font-size:28px;font-weight:700;padding:6px 64px 6px 20px;
  clip-path:polygon(0 0,86% 0,100% 100%,0 100%)}
.contact-list{position:absolute;left:60px;top:130px;list-style:none;font-size:17px;line-height:1.45}
.contact-list li{display:flex;gap:24px;margin-bottom:40px;align-items:flex-start}
.contact-list svg{flex:none;margin-top:2px}
.footer .brand{left:160px;top:408px}
.footer h4{position:absolute;top:84px;font-size:22px;font-weight:700}
.quick{position:absolute;left:552px;top:152px;list-style:none;font-size:15px}
.quick li{margin-bottom:24px}
.feedback{position:absolute;left:896px;top:160px;width:240px}
.feedback .field{height:36px;background:var(--white);margin-bottom:18px;font-size:14px;color:var(--muted);padding:8px 8px}
.feedback .field.area{height:110px}
.feedback .btn{font-size:15px;padding:6px 12px;border-radius:0}
.copyright{position:absolute;left:0;top:2560px;width:1200px;height:40px;background:#0d0d0f;color:var(--white);font-size:14px}
.copyright span.text{position:absolute;left:60px;top:10px}
.copyright .social{right:60px;top:11px}
</style>
</head>
<body>

<header class="hero" role="img" aria-label="Photo of hands on a broadcast mixing desk">
  <div class="brand"><span class="brand-mark"></span><span class="brand-name">Corvane</span></div>
  <div class="social"><span></span><span></span><span></span><span></span></div>
  <nav class="main-nav">
    <a class="active" href="#">Home</a><a href="#">About us</a><a href="#">Contact Us</a><a href="#">Gallery</a><a href="#">What We Do</a>
  </nav>
  <h1 class="hero-title">Broadcast &amp; AV System Installation</h1>
  <a class="btn" href="#">Read More</a>
  <svg class="arrow prev" viewBox="0 0 36 36"><circle cx="18" cy="18" r="17" fill="rgba(255,255,255,.85)"/><path d="M21 11l-7 7 7 7" stroke="#222" stroke-width="3" fill="none"/></svg>
  <svg class="arrow next" viewBox="0 0 36 36"><circle cx="18" cy="18" r="17" fill="rgba(255,255,255,.85)"/><path d="M15 11l7 7-7 7" stroke="#222" stroke-width="3" fill="none"/></svg>
  <div class="dots"><span></span><span></span><span></span><span></span></div>
</header>

<section class="services">
  <h2 class="section-title">Our Services</h2>
  <div class="rule"></div>
  <div class="service-list">
    <div class="service">
      <div class="service-icon"><svg width="44" height="44" viewBox="0 0 44 44"><rect x="6" y="8" width="32" height="22" rx="2" fill="#222"/><rect x="18" y="30" width="8" height="6" fill="#222"/><rect x="12" y="36" width="20" height="3" fill="#222"/></svg></div>
      <p>Broadcast/ AV<br>System Design</p>
    </div>
    <div class="service">
      <div class="service-icon"><svg width="44" height="44" viewBox="0 0 44 44"><circle cx="22" cy="22" r="12" fill="none" stroke="#222" stroke-width="6" stroke-dasharray="5 3"/><circle cx="22" cy="22" r="5" fill="#222"/></svg></div>
      <p>On-site<br>Installation</p>
    </div>
    <div class="service">
      <div class="service-icon"><svg width="44" height="44" viewBox="0 0 44 44"><rect x="8" y="6" width="28" height="9" rx="2" fill="#222"/><rect x="8" y="17" width="28" height="9" rx="2" fill="#222"/><rect x="8" y="28" width="28" height="9" rx="2" fill="#222"/></svg></div>
      <p>Rack Building</p>
    </div>
    <div class="service">
      <div class="service-icon"><svg width="44" height="44" viewBox="0 0 44 44"><path d="M8 34c6-16 14-4 20-18" stroke="#222" stroke-width="5" fill="none"/><rect x="26" y="6" width="10" height="12" rx="2" fill="#222"/></svg></div>
      <p>Pre-fabricated<br>Cable Looms</p>
    </div>
    <div class="service">
      <div class="service-icon"><svg width="44" height="44" viewBox="0 0 44 44"><path d="M6 30c10-2 18-10 30-20M10 36c10-4 18-12 28-18M8 24c8-2 14-8 22-16" stroke="#222" stroke-width="3" fill="none"/></svg></div>
      <p>Fibre-optic<br>Installation</p>
    </div>
  </div>
</section>

<section class="about">
  <h2>About Us</h2>
  <div class="underline"></div>
  <h3>Making the connection that digital innovation demands</h3>
  <p>Corvane provide cabling services for the Broadcast and Audio Visual industries. We specialise in the neat and clean installation which has come to be expected on high end systems. This helps us to achieve a robust and easily maintained installation that you can depend on.</p>
  <a class="btn btn-red" href="#">Read more</a>
  <div class="video" role="img" aria-label="Video still of engineers working on an installation"></div>
</section>

<section class="what">
  <div class="crowd" role="img" aria-label="Photo of a concert crowd with raised hands"></div>
  <h2>What We Do</h2>
  <div class="underline"></div>
  <ul>
    <li>Audio visual solutions for special events, fundraisers, meetings, conferences and conventions</li>
    <li>Professional sound systems for speech and entertainment</li>
    <li>Large screen projection with HD camera feeds and PowerPoint integration</li>
    <li>Media feeds for press conferences and stakeholder announcements</li>
    <li>Television specific lighting for media events</li>
    <li>Sound design and equipment rental for theatrical presentations</li>
    <li>Webcasting / Internet streaming and social media integration</li>
  </ul>
  <a class="btn" href="#">See What We Do</a>
</section>

<div class="quote">‘‘Making the connections that digital innovation demands ’’</div>

<footer class="footer">
  <div class="contact-tab">Contact Us</div>
  <ul class="contact-list">
    <li><svg width="22" height="28" viewBox="0 0 22 28"><path d="M11 1a9 9 0 0 0-9 9c0 7 9 17 9 17s9-10 9-17a9 9 0 0 0-9-9z" fill="var(--red)"/><circle cx="11" cy="10" r="3.5" fill="var(--dark)"/></svg><span>123 Street, Land Mark, Country,<br>123456</span></li>
    <li><svg width="24" height="18" viewBox="0 0 24 18"><rect x="1" y="1" width="22" height="16" rx="2" fill="none" stroke="var(--red)" stroke-width="2"/><path d="M1 2l11 8 11-8" stroke="var(--red)" stroke-width="2" fill="none"/></svg><span>info@corvane-example.com</span></li>
    <li><svg width="22" height="22" viewBox="0 0 22 22"><path d="M5 1l4 5-2 3c1 3 3 5 6 6l3-2 5 4-3 4C9 21 1 13 1 4z" fill="var(--red)"/></svg><span>01234 123-4567</span></li>
  </ul>
  <div class="brand"><span class="brand-mark"></span><span class="brand-name">Corvane</span></div>
  <h4 style="left:552px">Quick Links</h4>
  <ul class="quick"><li>Home</li><li>About us</li><li>Contact Us</li><li>Gallery</li><li>What We Do</li></ul>
  <h4 style="left:896px">Feedback</h4>
  <form class="feedback">
    <div class="field">Name</div>
    <div class="field">Email</div>
    <div class="field area">Message</div>
    <span class="btn btn-red">Send</span>
  </form>
</footer>

<div class="copyright">
  <span class="text">Copyright@corvane</span>
  <div class="social"><span></span><span></span><span></span><span></span></div>
</div>

</body>
</html>
```